PLANKHUB.NET Single Product Based Website

We are one of the largest Stockiest of Diesel Engine (Marine and Power Plants) Spare Parts, this site will be focusing on a Single Product / Spare Parts - Connecting Rods <br/>We attached some actual pictures of the product and the Logo,<br/><br/>Once we approved your design shall provide with some contends and 10 actual Pictures to be added , should be a single page website SEO friendly sources to be used<br/>Should be Desktop, laptop and mobile friendly <br/><br/>best regards<br/>Oliver <br/>

Coding

Coded - Design and coding required

Number of Pages Required

1 page

Font styles to use
Other font styles liked:
• Book Antigua, Book Man Old Style or the designer can suggest

Colors

Designer to choose colors to be used in the design.

Requirements
Must have
• The Logo and same theme / colors can be used
Nice to have
• We shall provide the actual pictures of the product from our gallery approx 10 pictures to be added at final stage
Should not have
• other than initial design purpose , do not use any pictures downloaded from the internet

```html
<!DOCTYPE html>
<html lang="en">
<head>
<meta charset="utf-8">
<title>PLANKHUB.NET – Diesel Engine Connecting Rods</title>
<link href="https://fonts.googleapis.com/css2?family=Lato:wght@400;700;900&family=Orbitron:wght@700;800&display=swap" rel="stylesheet">
<style>
:root{
  --orange:#f15a3b;
  --blue:#2d5aa0;
  --footer-blue:#335b9b;
  --ink:#1d1d1d;
  --body:#4a4a4a;
  --grey-bg:#e4e4e4;
  --line:#e2e2e2;
}
*{margin:0;padding:0;box-sizing:border-box}
html,body{width:1200px;height:3814px;overflow:hidden}
body{position:relative;font-family:"Lato",sans-serif;color:var(--ink);background:#fff}
.abs{position:absolute}
.btn{position:absolute;display:flex;align-items:center;justify-content:center;background:var(--orange);color:#fff;font-weight:700;font-size:16px;border-radius:20px;height:40px;width:163px}

/* hero */
.hero{left:0;top:0;width:1200px;height:560px;overflow:hidden}
.brand{position:absolute;left:141px;top:44px;font-weight:900;font-size:26px;letter-spacing:1px;color:var(--blue)}
.menu-btn{position:absolute;left:1010px;top:37px;width:48px;height:48px;border-radius:50%;background:#fff;display:flex;align-items:center;justify-content:center}
.hero h1{position:absolute;left:141px;top:198px;font-size:32px;line-height:41px;font-weight:900;color:#111;width:420px}
.rod-photo{position:absolute;left:490px;top:85px;width:420px;height:420px;border-radius:40px;background:linear-gradient(135deg,#dcdcdc,#8f9296);opacity:.9;transform:rotate(-40deg)}

/* section headings */
.sec-title{position:absolute;left:0;width:1200px;text-align:center;font-family:"Orbitron",sans-serif;font-weight:800;font-size:26px;letter-spacing:1px}
.sec-title .b{color:var(--blue)}
.sec-title .o{color:var(--orange)}

/* about */
.about-lead{position:absolute;left:0;top:710px;width:1200px;text-align:center;font-weight:700;font-size:15.5px}
.about-text{position:absolute;left:180px;top:746px;width:840px;text-align:center;font-size:12.5px;line-height:23.5px;color:var(--body)}

/* features */
.features{left:0;top:1033px;width:1200px;height:779px;background:linear-gradient(180deg,#e6e6e6,#dedede)}
.feature-rod{position:absolute;left:511px;top:1237px;width:170px;height:467px;border-radius:80px 80px 50px 50px;background:linear-gradient(90deg,#6f7377,#b9bcbf,#6c7074)}
.feat{position:absolute;width:190px}
.feat h3{font-size:16px;font-weight:700;margin-bottom:6px}
.feat p{font-size:11px;line-height:17px;color:#333}
.feat.left{text-align:right}
.feat-icon{position:absolute;width:88px;height:88px;border-radius:50%;border:1.5px dashed #9a9a9a;display:flex;align-items:center;justify-content:center}
.feat-icon span{width:68px;height:68px;border-radius:50%;background:#fff;display:flex;align-items:center;justify-content:center}

/* gallery */
.gallery{position:absolute;left:141px;top:1984px;width:918px;display:grid;grid-template-columns:repeat(4,1fr);grid-template-rows:repeat(4,211px);gap:7px}
.tile{width:100%;height:100%}

/* contact */
.map{left:0;top:3130px;width:1200px;height:460px;background:linear-gradient(180deg,#ececec,#dcdcdc)}
.contact-card{left:264px;top:3003px;width:671px;height:353px;background:#fff;box-shadow:0 4px 20px rgba(0,0,0,.06)}
.field{position:absolute;border:1px solid var(--line);height:38px;font-size:11.5px;color:#333;display:flex;align-items:center;gap:8px;padding-left:12px}
.field.area{align-items:flex-start;padding-top:12px}
.submit{position:absolute;left:610px;top:3253px;width:283px;height:39px;background:var(--blue);color:#fff;font-family:"Orbitron",sans-serif;font-weight:800;font-size:13px;display:flex;align-items:center;justify-content:center;letter-spacing:1px}

/* footer */
.footer{left:0;top:3590px;width:1200px;height:180px;background:var(--footer-blue);color:#fff}
.f-item{position:absolute;display:flex;gap:12px}
.f-icon{width:36px;height:36px;border-radius:50%;background:var(--orange);display:flex;align-items:center;justify-content:center;flex:none}
.f-item h4{font-family:"Orbitron",sans-serif;font-size:12px;font-weight:800;margin-bottom:4px}
.f-item p{font-size:12.5px;font-weight:700;line-height:20px}
.copyright{left:0;top:3770px;width:1200px;height:44px;background:var(--orange);color:#fff;font-size:12px;display:flex;align-items:center;justify-content:center}
</style>
</head>
<body>

<!-- HERO -->
<header class="abs hero">
  <svg class="abs" width="1200" height="560" role="img" aria-label="Greyscale diesel engine on the left and an orange-tinted container ship scene on the right">
    <defs>
      <linearGradient id="heroGrey" x1="0" y1="0" x2="1" y2="0">
        <stop offset="0" stop-color="#d8d8d8"/><stop offset="1" stop-color="#f3f3f3"/>
      </linearGradient>
    </defs>
    <rect width="1200" height="560" fill="url(#heroGrey)"/>
    <polygon points="904,0 1200,0 1200,560 530,560" fill="#f0684b"/>
  </svg>
  <div class="rod-photo" role="img" aria-label="Large marine engine connecting rod product photo"></div>
  <div class="brand">PLANKHUB.NET</div>
  <div class="menu-btn">
    <svg width="18" height="14"><rect width="18" height="2.5" fill="#f15a3b"/><rect y="5.7" width="18" height="2.5" fill="#f15a3b"/><rect y="11.4" width="18" height="2.5" fill="#f15a3b"/></svg>
  </div>
  <h1>We Are One of The Largest Stockiest of Diesel Engine Spare Parts</h1>
  <a class="btn" style="left:141px;top:348px">Call Us Today</a>
</header>

<!-- ABOUT -->
<h2 class="sec-title" style="top:657px"><span class="b">ABOUT</span>&nbsp;&nbsp;<span class="o">PLANKHUB.NET</span></h2>
<p class="about-lead">Tation ullamcorper suscipit lobortis nislt aliquip ex ea commodo consequat adipiscing elit</p>
<p class="about-text">Lorem ipsum dolor sit amet, consectetuer adipiscing elit, sed diam nonummy nibh euismod tincidunt ut laoreet dolore magna aliquam erat volutpat. Ut wisi enim ad minim veniam, quis nostrud exerci tation ullamcorper suscipit lobortis nislt aliquip ex ea commodo consequat. Duis autem vel eum iriure dolor in hendrerit in tation vulputate velit esse molestie consequat, vel illum dolore eu feugiat nulla facilisis vero eros et accumsan et iusto odio dignissim qui blandit praesent luptatum zzril delenit augue duis dolore te feugait nulla facilisis.</p>
<a class="btn" style="left:519px;top:881px">Call Us Today</a>

<!-- PRODUCT FEATURES -->
<section class="abs features"></section>
<h2 class="sec-title" style="top:1131px"><span class="b">PRODUCT</span>&nbsp;&nbsp;<span class="o">FEATURES</span></h2>
<div class="feature-rod" role="img" aria-label="Connecting rod product photo, standing upright"></div>

<div class="feat left" style="left:158px;top:1250px"><h3>Lorem Ipsum</h3><p>Lorem ipsum dolor sit dolai amet<br>consectetuer option adipiscing</p></div>
<div class="feat left" style="left:186px;top:1444px"><h3>Lorem Ipsum</h3><p>Lorem ipsum dolor sit dolai amet<br>consectetuer option adipiscing</p></div>
<div class="feat left" style="left:166px;top:1635px"><h3>Lorem Ipsum</h3><p>Lorem ipsum dolor sit dolai amet<br>consectetuer option adipiscing</p></div>
<div class="feat" style="left:853px;top:1250px"><h3>Lorem Ipsum</h3><p>Lorem ipsum dolor sit dolai amet<br>consectetuer option adipiscing</p></div>
<div class="feat" style="left:812px;top:1444px"><h3>Lorem Ipsum</h3><p>Lorem ipsum dolor sit dolai amet<br>consectetuer option adipiscing</p></div>
<div class="feat" style="left:819px;top:1635px"><h3>Lorem Ipsum</h3><p>Lorem ipsum dolor sit dolai amet<br>consectetuer option adipiscing</p></div>

<div class="feat-icon" style="left:369px;top:1236px"><span><svg width="34" height="32" fill="none" stroke="#f15a3b" stroke-width="1.5"><polygon points="10,2 16,2 19,7 16,12 10,12 7,7"/><polygon points="19,7 25,7 28,12 25,17 19,17 16,12"/><rect x="3" y="20" width="10" height="9"/><rect x="20" y="20" width="10" height="9"/></svg></span></div>
<div class="feat-icon" style="left:397px;top:1427px"><span><svg width="34" height="32" fill="none" stroke="#f15a3b" stroke-width="1.5"><polygon points="10,2 16,2 19,7 16,12 10,12 7,7"/><polygon points="19,7 25,7 28,12 25,17 19,17 16,12"/><rect x="3" y="20" width="10" height="9"/><rect x="20" y="20" width="10" height="9"/></svg></span></div>
<div class="feat-icon" style="left:377px;top:1618px"><span><svg width="34" height="32" fill="none" stroke="#f15a3b" stroke-width="1.5"><polygon points="10,2 16,2 19,7 16,12 10,12 7,7"/><polygon points="19,7 25,7 28,12 25,17 19,17 16,12"/><rect x="3" y="20" width="10" height="9"/><rect x="20" y="20" width="10" height="9"/></svg></span></div>
<div class="feat-icon" style="left:743px;top:1236px"><span><svg width="34" height="32" fill="none" stroke="#f15a3b" stroke-width="1.5"><polygon points="10,2 16,2 19,7 16,12 10,12 7,7"/><polygon points="19,7 25,7 28,12 25,17 19,17 16,12"/><rect x="3" y="20" width="10" height="9"/><rect x="20" y="20" width="10" height="9"/></svg></span></div>
<div class="feat-icon" style="left:701px;top:1427px"><span><svg width="34" height="32" fill="none" stroke="#f15a3b" stroke-width="1.5"><polygon points="10,2 16,2 19,7 16,12 10,12 7,7"/><polygon points="19,7 25,7 28,12 25,17 19,17 16,12"/><rect x="3" y="20" width="10" height="9"/><rect x="20" y="20" width="10" height="9"/></svg></span></div>
<div class="feat-icon" style="left:709px;top:1618px"><span><svg width="34" height="32" fill="none" stroke="#f15a3b" stroke-width="1.5"><polygon points="10,2 16,2 19,7 16,12 10,12 7,7"/><polygon points="19,7 25,7 28,12 25,17 19,17 16,12"/><rect x="3" y="20" width="10" height="9"/><rect x="20" y="20" width="10" height="9"/></svg></span></div>

<!-- GALLERY -->
<h2 class="sec-title" style="top:1910px"><span class="b">OUR</span>&nbsp;&nbsp;<span class="o">GALLERY</span></h2>
<div class="gallery">
  <div class="tile" style="background:linear-gradient(135deg,#e8c21e,#c9a414)" role="img" aria-label="Three blue connecting rods on a yellow sheet"></div>
  <div class="tile" style="grid-row:span 2;background:linear-gradient(180deg,#2b2b2b,#b8a98a)" role="img" aria-label="Two connecting rods lying on cardboard"></div>
  <div class="tile" style="grid-column:span 2;background:linear-gradient(135deg,#d4b9a3,#bca08a)" role="img" aria-label="Blue connecting rod on a beige floor"></div>
  <div class="tile" style="background:linear-gradient(135deg,#d8d8d8,#9b9b9b)" role="img" aria-label="Connecting rod big end close up"></div>
  <div class="tile" style="grid-row:span 2;background:linear-gradient(180deg,#4a4a4a,#6e6e6e)" role="img" aria-label="Silver connecting rod on dark mat"></div>
  <div class="tile" style="background:linear-gradient(135deg,#cdb79c,#6a6d72)" role="img" aria-label="Two connecting rods with labels"></div>
  <div class="tile" style="background:linear-gradient(135deg,#5d5a55,#8a8378)" role="img" aria-label="Rows of connecting rods in stock"></div>
  <div class="tile" style="background:linear-gradient(135deg,#8a7f74,#cfc8bf)" role="img" aria-label="Close up of a connecting rod cap"></div>
  <div class="tile" style="background:linear-gradient(135deg,#76706a,#b8b2aa)" role="img" aria-label="Many connecting rods arranged in rows"></div>
  <div class="tile" style="grid-column:span 4;background:linear-gradient(90deg,#a9a9a9,#c2c2c2,#a9a9a9)" role="img" aria-label="Connecting rod lying on grey concrete"></div>
</div>

<!-- CONTACT -->
<div class="abs map" role="img" aria-label="Street map of the company location"></div>
<section class="abs contact-card"></section>
<h2 class="sec-title" style="top:3079px"><span class="o">CONTACT</span>&nbsp;&nbsp;<span class="b">US</span></h2>
<div class="field" style="left:314px;top:3154px;width:282px">
  <svg width="11" height="11" fill="none" stroke="#f15a3b" stroke-width="1.3"><circle cx="5.5" cy="3.5" r="2.5"/><path d="M1 10.5c0-3 9-3 9 0"/></svg>Name</div>
<div class="field" style="left:314px;top:3204px;width:282px">
  <svg width="11" height="11" fill="none" stroke="#f15a3b" stroke-width="1.3"><path d="M2 1l2.5 0 1 3-1.5 1a6 6 0 0 0 3 3l1-1.5 3 1v2.5c-5 1-10-4-9-9z"/></svg>Phone</div>
<div class="field" style="left:314px;top:3254px;width:282px">
  <svg width="12" height="10" fill="none" stroke="#f15a3b" stroke-width="1.3"><rect x=".7" y=".7" width="10.6" height="8.6"/><path d="M1 1l5 4 5-4"/></svg>Email Address</div>
<div class="field area" style="left:610px;top:3153px;width:283px;height:92px">
  <svg width="11" height="11" fill="none" stroke="#f15a3b" stroke-width="1.3"><path d="M1 10l1-3 6-6 2 2-6 6z"/></svg>Phone</div>
<div class="submit">SUBMIT</div>

<!-- FOOTER -->
<footer class="abs footer">
  <div class="f-item" style="left:221px;top:73px">
    <span class="f-icon"><svg width="14" height="18" fill="#fff"><path d="M7 0a6 6 0 0 0-6 6c0 5 6 12 6 12s6-7 6-12a6 6 0 0 0-6-6zm0 8.5a2.5 2.5 0 1 1 0-5 2.5 2.5 0 0 1 0 5z"/></svg></span>
    <div><h4>PLANKHUB.NET</h4><p>123, Building Name, Street Name<br>City Name, State XY 123456</p></div>
  </div>
  <div class="f-item" style="left:558px;top:73px">
    <span class="f-icon"><svg width="16" height="16" fill="#fff"><path d="M3 1h3l1.5 4-2 1.3a8 8 0 0 0 4.2 4.2L11 8.5l4 1.5v3c0 1-1 2-2 2C7 15 1 9 1 3c0-1 1-2 2-2z"/></svg></span>
    <div><h4>PHONE</h4><p>+123 23 456 7890</p></div>
  </div>
  <div class="f-item" style="left:809px;top:76px">
    <span class="f-icon"><svg width="16" height="12" fill="#fff"><path d="M0 0h16v1.5L8 7 0 1.5z"/><path d="M0 3.5l8 5.5 8-5.5V12H0z"/></svg></span>
    <div><h4>EMAIL</h4><p>inquiry@plankhub.net</p></div>
  </div>
</footer>
<div class="abs copyright">Copyright © 2020&nbsp;<b>PLANKHUB</b>. All Rights Reserved.</div>

</body>
</html>
```